Business Card Design

We recently had a new logo designed by Pixel Harbor. Now we want to create new business cards and letterhead that compliment our new logo.

We are audiologists in private practice specializing in hearing evaluations and fitting hearing aids. We want a clean and professional card.

We need business cards for each audiologist. The names and titles are:
Marlene Voss-Kettering, AuD
Audiologist

Jane Pratt, AuD
Audiologist

Corinna Lundt, AuD
Audiologist

We also need a business card with no provider. Just a generic one.

Finally, we need an appointment card. This is what the front desk uses to give to the patient with their next appointment date and time.

Target Market(s)

Our clients tend to be highly educated. They are older so the cards should be clean and easy to read. No squirrely font please.

Industry/Entity Type

Business

Contact Information for Business Card

27831 Birchmont Dr NE, suite 418
Seattle, WA 98177
206-555-0182

Requirements
Must have
• Clean
Easy to read
Professional
Modern but approachable / warm
Should not have
• Other pictures besides the logo

```html
<!DOCTYPE html>
<html lang="en">
<head>
<meta charset="utf-8">
<title>Cedarline Hearing Services – Business and Appointment Cards</title>
<link href="https://fonts.googleapis.com/css2?family=Arimo:wght@400;700&display=swap" rel="stylesheet">
<style>
  :root {
    --page-bg: #ecebe8;
    --card-bg: #ffffff;
    --ink: #1d1d1f;
    --ink-soft: #6b6e73;
    --brand-grey: #4a4d52;
    --navy: #145674;
    --teal: #5cc2b0;
    --teal-deep: #33a794;
    --mark: #7b8ea6;
  }
  * { box-sizing: border-box; margin: 0; padding: 0; }
  html, body { width: 1200px; height: 914px; overflow: hidden; }
  body {
    background: var(--page-bg);
    font-family: "Arimo", Arial, sans-serif;
    color: var(--ink);
    display: flex;
    flex-direction: column;
    align-items: center;
    justify-content: center;
    gap: 40px;
  }
  .card {
    position: relative;
    width: 700px;
    height: 400px;
    background: var(--card-bg);
    box-shadow: 0 6px 18px rgba(0,0,0,.14);
    overflow: hidden;
  }
  .card__waves { position: absolute; inset: 0; width: 100%; height: 100%; }

  /* Front */
  .brand {
    position: absolute;
    top: 78px; left: 0; right: 0;
    display: flex; flex-direction: column; align-items: center;
  }
  .brand__lockup { display: flex; align-items: center; gap: 14px; }
  .brand__dot { width: 46px; height: 46px; border-radius: 50%; background: var(--mark); }
  .brand__name {
    font-size: 28px; font-weight: 700; color: var(--brand-grey);
    letter-spacing: 1px; text-transform: uppercase;
  }
  .brand__tagline {
    margin-top: 8px; font-size: 13px; color: var(--ink-soft);
    letter-spacing: 1.5px;
  }
  .contact {
    position: absolute; top: 172px; left: 0; right: 0;
    text-align: center; font-size: 17px; line-height: 1.45;
  }
  .provider {
    position: absolute; top: 308px; left: 100px; width: 380px;
    text-align: center;
  }
  .provider__name { font-size: 24px; line-height: 1.2; }
  .provider__title { font-size: 18px; line-height: 1.2; }

  /* Back */
  .appointment {
    position: absolute; top: 62px; left: 52px; right: 52px;
    font-size: 21px;
  }
  .field-row { display: flex; align-items: baseline; margin-bottom: 18px; }
  .field-label { white-space: nowrap; margin-right: 6px; }
  .field-line { flex: 1; border-bottom: 2px dotted var(--ink); height: 1px; }
  .field-row .field-line + .field-label { margin-left: 12px; }
</style>
</head>
<body>

  <section class="card card--front" aria-label="Business card front">
    <svg class="card__waves" viewBox="0 0 700 400" aria-hidden="true">
      <defs>
        <linearGradient id="teal-band" x1="0" x2="1" y1="0" y2="0">
          <stop offset="0" stop-color="var(--teal)"/>
          <stop offset="1" stop-color="var(--teal-deep)"/>
        </linearGradient>
      </defs>
      <path d="M0,262 Q360,238 700,392 L700,400 L0,400 Z" fill="url(#teal-band)"/>
      <path d="M0,238 Q360,210 700,370 L700,378 Q360,222 0,248 Z" fill="var(--navy)"/>
    </svg>

    <div class="brand">
      <div class="brand__lockup">
        <span class="brand__dot"></span>
        <span class="brand__name">Cedarline Hearing Services</span>
      </div>
      <p class="brand__tagline">Caring for how you hear</p>
    </div>

    <div class="contact">
      <p class="contact__phone">206-555-0182</p>
      <p class="contact__address">27831 Birchmont Dr NE, suite 418 Seattle, WA 98177</p>
    </div>

    <div class="provider">
      <p class="provider__name">Marlene Voss-Kettering, AuD</p>
      <p class="provider__title">Audiologist</p>
    </div>
  </section>

  <section class="card card--back" aria-label="Appointment card">
    <svg class="card__waves" viewBox="0 0 700 400" aria-hidden="true">
      <defs>
        <linearGradient id="teal-band-back" x1="0" x2="1" y1="0" y2="0">
          <stop offset="0" stop-color="var(--teal)"/>
          <stop offset="1" stop-color="var(--teal-deep)"/>
        </linearGradient>
      </defs>
      <path d="M0,262 Q360,238 700,392 L700,400 L0,400 Z" fill="url(#teal-band-back)"/>
      <path d="M0,238 Q360,210 700,370 L700,378 Q360,222 0,248 Z" fill="var(--navy)"/>
    </svg>

    <div class="appointment">
      <div class="field-row">
        <span class="field-label">Appointment :</span>
        <span class="field-line"></span>
      </div>
      <div class="field-row">
        <span class="field-label">Date :</span>
        <span class="field-line"></span>
        <span class="field-label">Time :</span>
        <span class="field-line"></span>
      </div>
    </div>
  </section>

</body>
</html>
```